Prepared Meal Delivery Website

Need a new modern design for a prepared meal delivery company that is hosted on Shopify.

Target Market(s)

Young Professionals

Industry/Entity Type

Prepared Meal Delivery Service

Number of Pages Required

5+ page

Requirements
Must have
• Use https://www.vorabelmeals.com/ as an example
Nice to have
• Vibrant page with call to action obvious and repeated
Should not have
• Generic look, grays/white/black

```html
<!DOCTYPE html>
<html lang="en">
<head>
<meta charset="utf-8">
<title>Dashway Meals — Prepared Meal Delivery</title>
<link href="https://fonts.googleapis.com/css2?family=Sanchez&family=Oswald:wght@400;500&family=Poppins:wght@400;500;600&display=swap" rel="stylesheet">
<style>
:root{
  --red:#e0201f;
  --yellow:#f6b73c;
  --orange:#f7a21b;
  --black:#0d0d0d;
  --ink:#1e1e1e;
  --white:#ffffff;
  --gray-bg:#f2f2f2;
  --pink-bg:#fde8e1;
  --cream-bg:#fdf5e6;
  --lime:#e6f0cf;
  --line:#c9c9c9;
}
*{margin:0;padding:0;box-sizing:border-box}
html,body{width:1200px;height:4170px;overflow:hidden}
body{position:relative;background:var(--white);font-family:"Poppins",sans-serif;color:var(--ink)}
.abs{position:absolute}
.serif{font-family:"Sanchez",serif}
.btn{position:absolute;display:flex;align-items:center;justify-content:center;background:var(--red);color:var(--white);border-radius:40px;font-family:"Oswald",sans-serif;font-size:27px;letter-spacing:2px;text-transform:uppercase}

/* nav */
.nav{position:absolute;left:0;top:0;width:1200px;height:89px;background:var(--black);z-index:5}
.brand{position:absolute;color:var(--white);font-family:"Poppins",sans-serif;font-weight:500;letter-spacing:4px;line-height:1;white-space:nowrap}
.nav .brand{left:112px;top:30px;font-size:26px}
.nav ul{position:absolute;right:112px;top:36px;display:flex;gap:22px;list-style:none;font-size:15px;font-weight:500;color:var(--white)}
.nav li.active{color:var(--orange)}

/* hero */
.hero-photo{position:absolute;left:0;top:89px;width:1200px;height:640px;background:linear-gradient(100deg,#4a2a16 0%,#6b4220 35%,#5b5a2a 60%,#4d6b2c 80%,#2f3d1d 100%)}
.hero-title{position:absolute;left:100px;top:148px;width:500px;text-align:center;color:var(--white);font-size:60px;line-height:1.15;text-transform:uppercase}
.hero-sub{position:absolute;left:110px;top:308px;width:476px;text-align:center;color:var(--white);font-size:19px;letter-spacing:1px}
.stat{position:absolute;color:var(--white);font-size:20px;font-weight:500;letter-spacing:1px;text-align:center;white-space:nowrap}
.dots{position:absolute;display:grid;gap:22px 28px}
.dots i{width:7px;height:7px;border-radius:50%;background:var(--white);display:block}

.phone{position:absolute;left:659px;top:155px;width:221px;height:482px;background:#151515;border-radius:30px;padding:9px;z-index:3}
.phone .screen{width:100%;height:100%;background:var(--white);border-radius:22px;position:relative;text-align:center}
.phone .brand{color:var(--black);left:0;width:100%;top:106px;font-size:18px;letter-spacing:3px;text-align:center}
.phone h4{position:absolute;left:0;width:100%;top:180px;font-size:16px;font-weight:500;line-height:1.5}
.phone p{position:absolute;left:14px;right:14px;top:238px;font-size:8px;line-height:1.5;color:#aaa}
.phone .pager{position:absolute;left:84px;top:340px;display:flex;gap:5px}
.phone .pager i{width:10px;height:4px;border-radius:2px;background:#ddd;display:block}
.phone .pager i.on{width:16px;background:var(--red)}
.phone .signin{position:absolute;left:16px;right:16px;top:383px;height:26px;font-size:15px;border-radius:14px}
.phone .new{position:absolute;left:0;width:100%;top:417px;font-size:8px;color:#555}

.badge{position:absolute;left:540px;top:683px;width:116px;height:116px;border-radius:50%;border:3px solid var(--black);background:var(--white);z-index:4}

/* how to order */
.sec-title{position:absolute;left:0;width:1200px;text-align:center;font-size:44px;letter-spacing:3px;text-transform:uppercase;color:var(--ink)}
.sec-desc{position:absolute;left:300px;width:600px;text-align:center;font-size:12.5px;line-height:1.75}
.steps{position:absolute;left:260px;top:972px;width:680px;height:170px;display:flex}
.step{flex:1;position:relative;text-align:center;border-left:2px solid var(--line)}
.step:first-child{border-left:none}
.step svg{margin-top:12px}
.step .num{display:block;margin:14px auto 0;width:24px;height:24px;border-radius:50%;background:var(--orange);color:var(--white);font-size:12px;line-height:24px;font-weight:600}
.step .s{display:block;font-family:"Oswald",sans-serif;font-size:14px;margin-top:10px;text-transform:uppercase}
.step .b{display:block;font-family:"Oswald",sans-serif;font-size:22px;text-transform:uppercase;line-height:1.1}

/* menu */
.menu{position:absolute;left:0;top:1194px;width:1200px;height:680px;background:var(--gray-bg)}
.tag{position:absolute;background:var(--yellow);font-family:"Oswald",sans-serif;font-size:20px;letter-spacing:1px;text-transform:uppercase;padding:1px 22px}
.card{position:absolute;border-radius:4px;overflow:hidden}
.card .label{position:absolute;color:var(--white);font-family:"Oswald",sans-serif;text-transform:uppercase;line-height:1.05}
.card .label em{font-style:normal;color:var(--yellow)}
.card .label .k{font-size:17px;display:block;margin-bottom:4px}

/* promo rows */
.promo-title{position:absolute;font-size:44px;line-height:1.2}
.promo-text{position:absolute;font-size:21px;line-height:1.5;width:500px}

/* reservation */
.field{position:absolute;width:333px;height:57px;border:2px solid var(--line);background:var(--white);font-family:"Oswald",sans-serif;font-size:15px;padding:18px 18px;text-transform:uppercase;color:#444}
.find{position:absolute;left:593px;top:3580px;width:332px;height:57px;background:var(--red);color:var(--white);font-family:"Oswald",sans-serif;font-size:26px;display:flex;align-items:center;justify-content:center;text-transform:uppercase}

/* footer */
.foot-h{position:absolute;color:var(--orange);font-size:19px;font-weight:600;text-transform:uppercase}
.foot-list{position:absolute;list-style:none;color:var(--white);font-size:17px;line-height:1.5;white-space:nowrap}
.foot-about{position:absolute;left:112px;top:4020px;width:520px;color:var(--white);font-size:21px;line-height:1.65;white-space:nowrap}
</style>
</head>
<body>

<header class="nav">
  <div class="brand">DASHWAY MEALS</div>
  <ul>
    <li class="active">HOME</li><li>HOW TO ORDER</li><li>FEATURES</li><li>GALLERY</li><li>CONTACTS</li>
  </ul>
</header>

<!-- hero -->
<div class="hero-photo" role="img" aria-label="Bowl of fresh vegetables on a rustic wooden table"></div>
<svg class="abs" style="left:0;top:580px" width="1200" height="330" viewBox="0 0 1200 330">
  <path d="M1200 40 C1120 30 1000 50 900 70 C1040 90 1140 170 1200 330 Z" fill="var(--lime)"/>
  <path d="M0 130 C140 170 300 160 440 140 C620 110 740 60 900 45 C1010 35 1110 70 1200 115 L1200 330 L0 330 Z" fill="var(--white)"/>
</svg>
<h1 class="hero-title serif">We get what<br>you love!</h1>
<p class="hero-sub">FROM YOUR FEVORITE RESTAURANTS</p>
<div class="btn" style="left:213px;top:376px;width:265px;height:67px;font-size:22px">Book now</div>

<svg class="abs" style="left:155px;top:492px" width="56" height="56" viewBox="0 0 56 56" fill="none" stroke="#fff" stroke-width="2.5"><circle cx="27" cy="27" r="24"/><path d="M27 12v15h10"/></svg>
<div class="stat" style="left:110px;top:565px">24/7 DELIVERY</div>
<svg class="abs" style="left:448px;top:496px" width="54" height="48" viewBox="0 0 54 48" fill="none" stroke="#fff" stroke-width="2.5"><path d="M6 4h42v8H6zM4 18h46M14 18v26M40 18v26M4 30h12M38 30h12M4 30v14M50 30v14"/></svg>
<div class="stat" style="left:360px;top:562px">2500 RESTAURANTS</div>
<svg class="abs" style="left:975px;top:496px" width="74" height="50" viewBox="0 0 74 50" fill="none" stroke="#fff" stroke-width="2.5"><path d="M22 10h28v26H22zM50 18h12l8 10v8H50zM2 16h16M6 24h14M10 32h10"/><circle cx="30" cy="40" r="5"/><circle cx="60" cy="40" r="5"/></svg>
<div class="stat" style="left:928px;top:560px">FAST DELIVERY</div>
<div class="dots" style="left:1143px;top:380px;grid-template-columns:7px 7px"><i></i><i></i><i></i><i></i><i></i><i></i><i></i><i></i></div>

<div class="phone">
  <div class="screen">
    <div class="brand">DASHWAY MEALS</div>
    <h4>Pick Up or Delivery<br>Restaurant</h4>
    <p>Order fresh meals from local kitchens and get them fast.</p>
    <div class="pager"><i></i><i class="on"></i><i></i></div>
    <div class="btn signin">Sign in</div>
    <div class="new">New Users? Sign Up</div>
  </div>
</div>

<div class="badge" role="img" aria-label="Brand badge"></div>

<!-- how to order -->
<h2 class="sec-title serif" style="top:820px">How to order?</h2>
<p class="sec-desc" style="top:888px">Lorem Ipsum is simply dummy text of the printing and typesetting industry. Lorem Ipsum has been the industry's standard dummy text ever since the 1500s</p>
<div class="steps">
  <div class="step">
    <svg width="46" height="50" viewBox="0 0 46 50" fill="none" stroke="#333" stroke-width="2"><rect x="6" y="14" width="34" height="30" rx="3"/><path d="M2 46h42M16 22a10 10 0 0 1 14 0M19 27a5 5 0 0 1 8 0"/><circle cx="23" cy="33" r="2"/></svg>
    <span class="num">1</span><span class="s">Choose your</span><span class="b">Location</span>
  </div>
  <div class="step">
    <svg width="46" height="50" viewBox="0 0 46 50" fill="none" stroke="#333" stroke-width="2"><rect x="4" y="4" width="38" height="42" rx="2"/><path d="M23 4v42M12 12v12M9 12v6h6v-6M32 12h6M32 18h6M32 24h6"/></svg>
    <span class="num">2</span><span class="s">Choose</span><span class="b">Restaurant</span>
  </div>
  <div class="step">
    <svg width="46" height="50" viewBox="0 0 46 50" fill="none" stroke="#333" stroke-width="2"><path d="M8 22h30l-3 24H11zM14 22V12h18v10M30 4l-4 8"/><path d="M12 32h22M12 38h22"/></svg>
    <span class="num">3</span><span class="s">Make your</span><span class="b">Order</span>
  </div>
  <div class="step">
    <svg width="56" height="50" viewBox="0 0 56 50" fill="none" stroke="#333" stroke-width="2"><path d="M6 28h26l4-12h8M18 20h10v8H18z"/><circle cx="12" cy="38" r="6"/><circle cx="44" cy="38" r="6"/><path d="M32 28l6 10"/><circle cx="36" cy="8" r="4"/></svg>
    <span class="num">4</span><span class="s">Food is on</span><span class="b">The way</span>
  </div>
</div>

<!-- popular menu -->
<section class="menu">
  <div class="tag" style="left:511px;top:46px">Popular menu</div>
  <h2 class="sec-title serif" style="top:92px">Fresh delicacies</h2>
  <div class="card" style="left:60px;top:194px;width:523px;height:368px;background:radial-gradient(circle at 68% 55%,#c8643a 0%,#8a3b22 28%,#2a2a2a 55%,#141414 100%)" role="img" aria-label="Colourful pasta salad with tomatoes and basil on a dark table">
    <div class="label" style="left:22px;top:112px"><span class="k">Try it today</span><span style="font-size:30px">Popular <em>pasta salad</em></span></div>
  </div>
  <div class="card" style="left:620px;top:194px;width:524px;height:170px;background:linear-gradient(90deg,#2b2b2b 0%,#4a4a3a 40%,#9a8a3a 60%,#5b6b2b 80%,#3a2a3a 100%)" role="img" aria-label="Bowl with avocado, chickpeas and greens">
    <div class="label" style="left:26px;top:24px"><span class="k">Try it today</span><span style="font-size:30px">More <em>fun</em><br>More <em>taste</em></span></div>
  </div>
  <div class="card" style="left:620px;top:395px;width:524px;height:167px;background:linear-gradient(90deg,#1a1a1a 0%,#2c2a20 45%,#7a4a22 70%,#3d5a25 85%,#d8d8d0 100%)" role="img" aria-label="Plate of chili chicken with rice and broccoli">
    <div class="label" style="left:26px;top:62px"><span class="k">Try it today</span><span style="font-size:30px">Fresh &amp; <em>chili</em></span></div>
  </div>
</section>

<!-- discount -->
<div class="abs" style="left:0;top:1874px;width:617px;height:616px;background:radial-gradient(circle at 45% 48%,#9ec55a 0%,#f2f2f0 32%,#e8e8e6 40%,#8a6a4a 55%,#5a3e28 100%)" role="img" aria-label="Avocado toast with cherry tomatoes on a white plate"></div>
<div class="abs" style="left:617px;top:1874px;width:583px;height:616px;background:var(--pink-bg)"></div>
<h3 class="promo-title serif" style="left:661px;top:1985px">Discount up to<br>20% All Menu</h3>
<p class="promo-text" style="left:663px;top:2118px">Lorem ipsum dolor sit amet, consectetuer adipiscing elit, sed diam nonummy nibh euismod tincidunt ut laoreet dolore magna aliquam erat volutpat.</p>
<div class="btn" style="left:664px;top:2294px;width:294px;height:65px">Read more</div>

<!-- august -->
<div class="abs" style="left:0;top:2490px;width:619px;height:682px;background:var(--cream-bg)"></div>
<div class="abs" style="left:619px;top:2490px;width:581px;height:682px;background:linear-gradient(160deg,#1e2a1a 0%,#3d6a2a 30%,#8a5a30 55%,#4a3020 80%,#1a1a1a 100%)" role="img" aria-label="Grilled chicken and zucchini skewers on a wooden board"></div>
<div class="dots" style="left:979px;top:3108px;grid-template-columns:repeat(5,7px);gap:18px 30px"><i></i><i></i><i></i><i></i><i></i><i></i><i></i><i></i><i></i><i></i></div>
<h3 class="promo-title serif" style="left:108px;top:2657px">August Specials<br>Buy 1 Get 1 Free!</h3>
<p class="promo-text" style="left:111px;top:2796px">Lorem ipsum dolor sit amet, consectetuer adipiscing elit, sed diam nonummy nibh euismod tincidunt ut laoreet dolore magna aliquam erat volutpat.</p>
<div class="btn" style="left:110px;top:2977px;width:293px;height:65px">Read more</div>

<!-- reservation -->
<div class="abs" style="left:-30px;top:3210px;width:146px;height:170px;border-radius:50%;background:radial-gradient(circle at 40% 35%,#f0b04a 0%,#c7701f 70%,#8a4a18 100%)" role="img" aria-label="Burger"></div>
<div class="abs" style="left:92px;top:3408px;width:66px;height:236px;border-radius:14px 14px 22px 22px;background:linear-gradient(90deg,#5a0c0c,#b3161a,#6a0e0e)" role="img" aria-label="Bottle of hot sauce"></div>
<div class="abs" style="left:1005px;top:3450px;width:260px;height:300px;border-radius:50%;background:radial-gradient(circle at 40% 55%,#d58a2a 0%,#c7701f 30%,#f2e6d0 55%,#f5ece0 100%)" role="img" aria-label="Plate with burger, fries and ketchup"></div>
<div class="tag" style="left:506px;top:3257px">Reservation</div>
<h2 class="sec-title serif" style="top:3302px">Book your table</h2>
<div class="field" style="left:236px;top:3418px">Name</div>
<div class="field" style="left:593px;top:3418px">Email</div>
<div class="field" style="left:236px;top:3499px">Date</div>
<div class="field" style="left:593px;top:3499px">Time</div>
<div class="field" style="left:236px;top:3580px">People</div>
<div class="find">Find a table</div>

<!-- footer -->
<svg class="abs" style="left:0;top:3580px" width="1200" height="590" viewBox="0 0 1200 590">
  <path d="M0 0 C60 60 140 120 260 170 C420 230 620 230 820 200 L0 240 Z" fill="var(--yellow)"/>
  <path d="M0 40 C80 110 170 160 300 200" stroke="#fff" stroke-width="4" fill="none"/>
  <path d="M0 215 C300 245 560 230 760 200 C940 170 1080 110 1200 80 L1200 590 L0 590 Z" fill="var(--black)"/>
</svg>
<div class="brand" style="left:829px;top:3852px;font-size:32px;letter-spacing:5px">DASHWAY MEALS</div>
<div class="foot-h" style="left:112px;top:3958px">About</div>
<p class="foot-about">Lorem ipsum dolor sit amet, consec<br>tetur adipisicing elit, sed do eiusmod tempor<br>incididunt ultimam quantum</p>
<div class="foot-h" style="left:661px;top:3957px;font-size:17px">Menu1</div>
<ul class="foot-list" style="left:661px;top:4014px"><li>How to order</li><li>Features</li><li>Gallery</li><li>Contact</li></ul>
<div class="foot-h" style="left:826px;top:3957px;font-size:17px">Menu2</div>
<ul class="foot-list" style="left:826px;top:4014px"><li>Our Story</li><li>Partners</li><li>How It Works</li><li>Meals</li></ul>
<div class="foot-h" style="left:988px;top:3957px;font-size:17px">Menu3</div>
<ul class="foot-list" style="left:990px;top:4014px"><li>Testimonials</li><li>Press</li><li>Careers</li><li>Fitness &amp; health</li></ul>

</body>
</html>
```